Our Vitaleaf - Health and Wellbeing

ABOUT US
we are a supplements and health foods business
Vegan, Lactose, Gluten friendly products
Clean and healthy living approach/mentality

We will be using both 1kg and 500g rectangle bags.
The types of products
Pea Protein
Rice Protein
Hemp Protein
Soy Protein
Creatine
Spirulina

The design needs to be able to facilitate change of product text

1kg
Length: 335 mm
Width: 240 mm
Bottom Gusset: 100 mm

500g
Length: 275 mm
Width: 190 mm
Bottom Gusset: 90 mm

REQUIREMENTS
Digital Banners (inc facebook & Instagram)
Product Label
Branding

CREATIVE IDEAS
colorful and bright
community values, social conscience
crisp/sharp/fresh feeling
dark text with splashes of bright/color throughout
results/success
Use of props, leaves, nature etc.

Target Market(s)

Vegan and health conscience consumers

Industry/Entity Type

Business

Font styles to use
Sans Serif
Decorative
Script

Colors
86cfc6
add136
fbee3e
faa54b
f04a50
33a6d7

Requirements
Must have
• community values, social conscience
• TEXT
• Vegan
• Plant based
• raw
• natural
• gluten free
• Lactose free
• organic ingredients
Nice to have
• Use of props, leaves, nature etc.
• Open to changing the colour scheme of the logo.
• Feature of the text to be around each product, logo secondary on the label.
Should not have
• dark colours
• simple design

```html
<!DOCTYPE html>
<html lang="en">
<head>
<meta charset="utf-8">
<title>Our Vitaleaf – Protein Bag Labels</title>
<link href="https://fonts.googleapis.com/css2?family=Amatic+SC:wght@700&family=Montserrat:wght@400;700&display=swap" rel="stylesheet">
<style>
  :root {
    --pea: #1eaee0;
    --rice: #f27a66;
    --paper: #ffffff;
    --label-white: rgba(250, 250, 248, 0.86);
    --band-white: rgba(255, 255, 255, 0.85);
    --caption: rgba(255, 255, 255, 0.92);
  }
  html, body {
    margin: 0;
    padding: 0;
    width: 1200px;
    height: 1200px;
    overflow: hidden;
    background: var(--paper);
  }
  .canvas {
    position: relative;
    width: 1200px;
    height: 1200px;
  }
  .bag-front {
    position: absolute;
    top: 12px;
    width: 580px;
    height: 1174px;
  }
  .bag-front--pea { left: 14px; --accent: var(--pea); }
  .bag-front--rice { left: 606px; --accent: var(--rice); }
  .bag-front svg { display: block; width: 580px; height: 1174px; }
  .colour-block { fill: var(--accent); }
  .label-banner { fill: var(--label-white); stroke: var(--accent); stroke-width: 1.5; }
  .label-rule { stroke: var(--accent); stroke-width: 3; }
  .ornament { fill: var(--accent); opacity: 0.85; }
  .product-title {
    font-family: "Amatic SC", "Arial Narrow", sans-serif;
    font-weight: 700;
    fill: var(--accent);
    text-anchor: middle;
  }
  .info-band { fill: var(--band-white); }
  .claim-icon { fill: var(--accent); }
  .claim-icon-mark { fill: none; stroke: #fff; stroke-width: 2; stroke-linecap: round; }
  .claim-icon-letters {
    font-family: "Montserrat", sans-serif;
    font-weight: 700;
    font-size: 13px;
    fill: #fff;
    text-anchor: middle;
  }
  .claim-caption {
    font-family: "Montserrat", sans-serif;
    font-weight: 400;
    font-size: 10.5px;
    fill: var(--caption);
  }
  .seal-outer { fill: var(--paper); stroke: var(--accent); stroke-width: 10; }
  .seal-ring { fill: none; stroke: var(--accent); stroke-width: 5; stroke-dasharray: 5 4; }
  .seal-inner { fill: var(--paper); stroke: var(--accent); stroke-width: 1.5; }
  .brand-name {
    font-family: "Montserrat", sans-serif;
    font-weight: 700;
    font-size: 20px;
    fill: var(--accent);
    text-anchor: middle;
  }
</style>
</head>
<body>
<main class="canvas">

  <!-- Pea protein bag front -->
  <section class="bag-front bag-front--pea">
    <svg viewBox="0 0 580 1174" xmlns="http://www.w3.org/2000/svg">
      <defs>
        <linearGradient id="peaPhoto" x1="0" y1="0" x2="1" y2="1">
          <stop offset="0" stop-color="#4f8a3c"/>
          <stop offset="0.35" stop-color="#7fb25a"/>
          <stop offset="0.6" stop-color="#d9e6cf"/>
          <stop offset="1" stop-color="#3f7a34"/>
        </linearGradient>
      </defs>
      <rect class="product-photo" x="0" y="0" width="580" height="900" fill="url(#peaPhoto)" role="img" aria-label="Photograph of flowering pea plants with white blossoms and green leaves"/>
      <rect class="colour-block" x="0" y="900" width="580" height="274"/>

      <g class="product-label">
        <polygon class="label-banner" points="181,0 400,0 400,470 290,584 181,470"/>
        <rect class="ornament" x="228" y="38" width="124" height="60" rx="30" role="img" aria-label="Decorative flourish"/>
        <line class="label-rule" x1="222" y1="108" x2="358" y2="108"/>
        <text class="product-title" x="290" y="176" font-size="72" textLength="136" lengthAdjust="spacingAndGlyphs">ORGANIC</text>
        <line class="label-rule" x1="222" y1="187" x2="358" y2="187"/>
        <text class="product-title" x="290" y="328" font-size="164" textLength="128" lengthAdjust="spacingAndGlyphs">PEA</text>
        <text class="product-title" x="290" y="406" font-size="85" textLength="136" lengthAdjust="spacingAndGlyphs">PROTEIN</text>
        <line class="label-rule" x1="222" y1="421" x2="358" y2="421"/>
        <text class="product-title" x="290" y="450" font-size="23" textLength="140" lengthAdjust="spacingAndGlyphs">RAW | VEGAN | GLUTEN FREE</text>
        <line class="label-rule" x1="222" y1="462" x2="358" y2="462"/>
        <rect class="ornament" x="228" y="470" width="124" height="60" rx="30" role="img" aria-label="Decorative flourish"/>
      </g>

      <rect class="info-band" x="0" y="720" width="580" height="78"/>
      <g class="claim-icons">
        <circle class="claim-icon" cx="36" cy="758" r="20"/><circle class="claim-icon-mark" cx="36" cy="758" r="7"/>
        <circle class="claim-icon" cx="90" cy="758" r="20"/><path class="claim-icon-mark" d="M90 768 V754 M90 756 q-8 -2 -9 -9 q8 0 9 9 M90 756 q8 -2 9 -9 q-8 0 -9 9"/>
        <circle class="claim-icon" cx="144" cy="758" r="20"/><path class="claim-icon-mark" d="M137 749 L144 768 L152 747"/>
        <circle class="claim-icon" cx="436" cy="758" r="20"/><text class="claim-icon-letters" x="436" y="763">GF</text>
        <circle class="claim-icon" cx="491" cy="758" r="20"/><path class="claim-icon-mark" d="M486 768 V750 M491 768 V747 M496 768 V752"/>
        <circle class="claim-icon" cx="544" cy="758" r="20"/><text class="claim-icon-letters" x="544" y="763">LF</text>
      </g>
      <text class="claim-caption" x="16" y="818">Organic | Plant Based | Vegan</text>
      <text class="claim-caption" x="568" y="818" text-anchor="end">Gluten Free | Raw | Lactose Free</text>

      <g class="brand-seal">
        <circle class="seal-outer" cx="290" cy="746" r="110"/>
        <circle class="seal-ring" cx="290" cy="746" r="94"/>
        <circle class="seal-inner" cx="290" cy="746" r="84"/>
        <text class="brand-name" x="290" y="753">Our Vitaleaf</text>
      </g>
    </svg>
  </section>

  <!-- Rice protein bag front -->
  <section class="bag-front bag-front--rice">
    <svg viewBox="0 0 580 1174" xmlns="http://www.w3.org/2000/svg">
      <defs>
        <linearGradient id="ricePhoto" x1="0" y1="0" x2="0" y2="1">
          <stop offset="0" stop-color="#eef0ee"/>
          <stop offset="0.15" stop-color="#6b7468"/>
          <stop offset="0.3" stop-color="#9cc26a"/>
          <stop offset="0.7" stop-color="#5e9a2e"/>
          <stop offset="1" stop-color="#2f5a1c"/>
        </linearGradient>
      </defs>
      <rect class="product-photo" x="0" y="0" width="580" height="900" fill="url(#ricePhoto)" role="img" aria-label="Photograph of dewy green rice grass with a misty tree line behind"/>
      <rect class="colour-block" x="0" y="900" width="580" height="274"/>

      <g class="product-label">
        <polygon class="label-banner" points="181,0 400,0 400,470 290,584 181,470"/>
        <rect class="ornament" x="228" y="38" width="124" height="60" rx="30" role="img" aria-label="Decorative flourish"/>
        <line class="label-rule" x1="222" y1="108" x2="358" y2="108"/>
        <text class="product-title" x="290" y="176" font-size="72" textLength="136" lengthAdjust="spacingAndGlyphs">ORGANIC</text>
        <line class="label-rule" x1="222" y1="187" x2="358" y2="187"/>
        <text class="product-title" x="290" y="328" font-size="164" textLength="132" lengthAdjust="spacingAndGlyphs">RICE</text>
        <text class="product-title" x="290" y="406" font-size="85" textLength="136" lengthAdjust="spacingAndGlyphs">PROTEIN</text>
        <line class="label-rule" x1="222" y1="421" x2="358" y2="421"/>
        <text class="product-title" x="290" y="450" font-size="23" textLength="140" lengthAdjust="spacingAndGlyphs">RAW | VEGAN | GLUTEN FREE</text>
        <line class="label-rule" x1="222" y1="462" x2="358" y2="462"/>
        <rect class="ornament" x="228" y="470" width="124" height="60" rx="30" role="img" aria-label="Decorative flourish"/>
      </g>

      <rect class="info-band" x="0" y="720" width="580" height="78"/>
      <g class="claim-icons">
        <circle class="claim-icon" cx="36" cy="758" r="20"/><circle class="claim-icon-mark" cx="36" cy="758" r="7"/>
        <circle class="claim-icon" cx="90" cy="758" r="20"/><path class="claim-icon-mark" d="M90 768 V754 M90 756 q-8 -2 -9 -9 q8 0 9 9 M90 756 q8 -2 9 -9 q-8 0 -9 9"/>
        <circle class="claim-icon" cx="144" cy="758" r="20"/><path class="claim-icon-mark" d="M137 749 L144 768 L152 747"/>
        <circle class="claim-icon" cx="436" cy="758" r="20"/><text class="claim-icon-letters" x="436" y="763">GF</text>
        <circle class="claim-icon" cx="491" cy="758" r="20"/><path class="claim-icon-mark" d="M486 768 V750 M491 768 V747 M496 768 V752"/>
        <circle class="claim-icon" cx="544" cy="758" r="20"/><text class="claim-icon-letters" x="544" y="763">LF</text>
      </g>
      <text class="claim-caption" x="16" y="818">Organic | Plant Based | Vegan</text>
      <text class="claim-caption" x="568" y="818" text-anchor="end">Gluten Free | Raw | Lactose Free</text>

      <g class="brand-seal">
        <circle class="seal-outer" cx="290" cy="746" r="110"/>
        <circle class="seal-ring" cx="290" cy="746" r="94"/>
        <circle class="seal-inner" cx="290" cy="746" r="84"/>
        <text class="brand-name" x="290" y="753">Our Vitaleaf</text>
      </g>
    </svg>
  </section>

</main>
</body>
</html>
```